Update New Business Card - For Start Up

I need to update my business card, I have our old version for example. I would like to keep to the same colors and theme. We are a threat reporting and case management tool for corporations and educational institutions.

Target Market(s)

Corporate Security and Human Resources, School Administrators and Superintendents.

Industry/Entity Type

Physical Security and Technology.

Contact Information for Business Card

My Name, Founder/CEO, phone number 777-412-5068, Logo, Web...

Colors
0054AA
0677BA
7BADD7
CADEEF
E8F1F8

Requirements
Must have
• Something new and trendy.

```html
<!DOCTYPE html>
<html lang="en">
<head>
<meta charset="utf-8">
<title>Velmora Business Card</title>
<link rel="stylesheet" href="https://fonts.googleapis.com/css2?family=Roboto+Condensed:wght@400;700&family=Roboto:wght@700&display=swap">
<style>
  :root {
    --brand-blue: #1e75bb;
    --deep-blue: #0054aa;
    --light-blue: #7badd7;
    --pale-blue: #cadeef;
    --paper: #ffffff;
    --backdrop: #f0f0f0;
    --ink-grey: #666666;
  }
  * { margin: 0; padding: 0; box-sizing: border-box; }
  html, body {
    width: 1200px; height: 871px; overflow: hidden;
    background: var(--backdrop);
  }
  .card {
    position: absolute; left: 294px;
    width: 609px; height: 348px; overflow: hidden;
  }
  .card--front { top: 43px; background: var(--paper); }
  .card--back { top: 460px; background: var(--brand-blue); }

  .corner-texture { position: absolute; width: 134px; height: 83px; }
  .corner-texture--top { left: 0; top: 0; }
  .corner-texture--bottom { right: 0; bottom: 0; }
  .card--front .corner-texture--top { background: linear-gradient(160deg, var(--brand-blue) 35%, rgba(123,173,215,0) 100%); }
  .card--front .corner-texture--bottom { background: linear-gradient(340deg, var(--brand-blue) 35%, rgba(123,173,215,0) 100%); }
  .card--back .corner-texture--top { background: linear-gradient(160deg, var(--paper) 25%, rgba(255,255,255,0) 100%); }
  .card--back .corner-texture--bottom { background: linear-gradient(340deg, var(--paper) 25%, rgba(255,255,255,0) 100%); }

  .brand-mark {
    position: absolute; left: 62px; top: 110px; width: 156px;
    display: flex; flex-direction: column; align-items: center; gap: 12px;
  }
  .brand-mark__dot { width: 100px; height: 100px; border-radius: 50%; background: var(--brand-blue); }
  .brand-mark__name {
    font-family: "Roboto Condensed", sans-serif; font-weight: 700;
    font-size: 26px; letter-spacing: 3px; color: var(--brand-blue);
  }

  .divider {
    position: absolute; left: 252px; top: 59px;
    width: 4px; height: 231px; background: var(--brand-blue);
  }

  .identity { position: absolute; left: 283px; top: 56px; }
  .identity__name {
    font-family: "Roboto Condensed", sans-serif; font-weight: 700;
    font-size: 32px; line-height: 32px; color: var(--brand-blue);
  }
  .identity__role {
    font-family: "Roboto Condensed", sans-serif; font-weight: 400;
    font-size: 20px; line-height: 18px; color: var(--ink-grey);
  }

  .contacts { position: absolute; left: 286px; top: 147px; list-style: none; }
  .contacts__item {
    display: flex; align-items: center; gap: 14px; height: 28px; margin-bottom: 19px;
    font-family: "Roboto", sans-serif; font-weight: 700; font-size: 21px; color: var(--ink-grey);
  }
  .contacts__icon { width: 28px; height: 28px; flex: none; }

  .wordmark {
    position: absolute; left: 94px; top: 130px;
    display: flex; align-items: center; gap: 28px;
  }
  .wordmark__dot { width: 88px; height: 88px; border-radius: 50%; background: var(--paper); }
  .wordmark__name {
    font-family: "Roboto Condensed", sans-serif; font-weight: 400;
    font-size: 48px; letter-spacing: 12px; color: var(--paper);
  }
</style>
</head>
<body>

<section class="card card--front">
  <div class="corner-texture corner-texture--top" role="img" aria-label="Scattered square pixel pattern fading from the corner"></div>
  <div class="brand-mark">
    <div class="brand-mark__dot"></div>
    <div class="brand-mark__name">VELMORA</div>
  </div>
  <div class="divider"></div>
  <div class="identity">
    <div class="identity__name">LENA VARTON</div>
    <div class="identity__role">CHIEF EXECUTIVE OFFICER</div>
  </div>
  <ul class="contacts">
    <li class="contacts__item">
      <svg class="contacts__icon" viewBox="0 0 28 28" aria-hidden="true">
        <circle cx="14" cy="14" r="14" fill="var(--brand-blue)"/>
        <path d="M9 8.5c1-1 2-1 2.6 0l1.2 2c.4.7.2 1.3-.4 1.8l-.8.6c.7 1.6 2 2.9 3.6 3.6l.6-.8c.5-.6 1.1-.8 1.8-.4l2 1.2c1 .6 1 1.6 0 2.6-1 1-2.4 1.3-4 .6-3.2-1.4-5.8-4-7.2-7.2-.7-1.6-.4-3 .6-4z" fill="var(--paper)"/>
      </svg>
      777-412-5068
    </li>
    <li class="contacts__item">
      <svg class="contacts__icon" viewBox="0 0 28 28" aria-hidden="true">
        <circle cx="14" cy="14" r="14" fill="var(--brand-blue)"/>
        <rect x="7" y="9" width="14" height="10" fill="none" stroke="var(--paper)" stroke-width="1.4"/>
        <path d="M7 9l7 6 7-6M7 19l5-5M21 19l-5-5" fill="none" stroke="var(--paper)" stroke-width="1.4"/>
      </svg>
      lena@velmora.co
    </li>
    <li class="contacts__item">
      <svg class="contacts__icon" viewBox="0 0 28 28" aria-hidden="true">
        <circle cx="14" cy="14" r="14" fill="var(--brand-blue)"/>
        <g fill="none" stroke="var(--paper)" stroke-width="1.2">
          <circle cx="14" cy="14" r="7.5"/>
          <ellipse cx="14" cy="14" rx="3.2" ry="7.5"/>
          <path d="M6.5 14h15M7.5 10.5h13M7.5 17.5h13M14 6.5v15"/>
        </g>
      </svg>
      www.velmora.co
    </li>
  </ul>
  <div class="corner-texture corner-texture--bottom" role="img" aria-label="Scattered square pixel pattern fading from the corner"></div>
</section>

<section class="card card--back">
  <div class="corner-texture corner-texture--top" role="img" aria-label="Scattered square pixel pattern fading from the corner"></div>
  <div class="wordmark">
    <div class="wordmark__dot"></div>
    <div class="wordmark__name">VELMORA</div>
  </div>
  <div class="corner-texture corner-texture--bottom" role="img" aria-label="Scattered square pixel pattern fading from the corner"></div>
</section>

</body>
</html>
```